Orlend Structural Approval Standards Private Assessors

Professional Construction Consultancy Company Business Card - must keep logo colours see images below - examples have been added from my last competition - please see them as examples only!

Target Market(s)

Home Builders

Industry/Entity Type

Construction

Contact Information for Business Card

See "must haves"

Font styles to use
Sans Serif

Colors
ffffff
add136
000000

Requirements
Must have
• Daniel Moravi
• Director
• Phone: 0431 587 219
• Address: 7 Tarrunga Rd,
• Hallworth Vale, SA, 5091
• Email: orlendassessors@mailbox-example.com
• Website: www.orlendassessors-example.com.au
• Facebook: Orlend Structural Approval Standards
Nice to have
• Side 1: full logo
• Side 2: company details
Should not have
• hard to read
• must be clear and professional

```html
<!DOCTYPE html>
<html lang="en">
<head>
<meta charset="utf-8">
<title>Orlend Structural Approval Standards – Business Card</title>
<link rel="stylesheet" href="https://fonts.googleapis.com/css2?family=Montserrat:wght@500;700&family=Questrial&display=swap">
<style>
  :root {
    --green: #add136;
    --green-light: #c3e06a;
    --black: #000000;
    --ink: #1c1c1c;
    --text-grey: #3a3a3a;
    --white: #ffffff;
    --paper: #f4f4f4;
    --backdrop: #3b3b3b;
  }
  * { margin: 0; padding: 0; box-sizing: border-box; }
  html, body {
    width: 1200px; height: 900px; overflow: hidden;
    background: var(--backdrop);
  }
  .stage { position: relative; width: 1200px; height: 900px; }
  .card {
    position: absolute; left: 303px; width: 594px; height: 325px;
    box-shadow: 0 4px 14px rgba(0,0,0,0.45);
    overflow: hidden;
  }
  /* Side 1 */
  .card-front {
    top: 102px;
    background: radial-gradient(ellipse at 55% 55%, var(--green-light), var(--green) 70%);
  }
  .front-brand {
    position: absolute; left: 0; right: 0; top: 126px;
    display: flex; align-items: center; justify-content: center; gap: 12px;
  }
  .brand-square { width: 44px; height: 44px; background: var(--black); flex: none; }
  .brand-name {
    font-family: "Montserrat", sans-serif; font-weight: 700;
    color: var(--black); text-transform: uppercase;
    font-size: 17px; line-height: 1.18; letter-spacing: 0.5px;
  }
  .front-social {
    position: absolute; left: 0; right: 0; top: 273px;
    display: flex; align-items: center; justify-content: center; gap: 8px;
    font-family: "Questrial", sans-serif; font-size: 15px;
    color: var(--ink); letter-spacing: 0.6px;
  }
  .social-square { width: 16px; height: 16px; background: var(--ink); border-radius: 2px; }
  /* Side 2 */
  .card-back {
    top: 472px;
    background: linear-gradient(180deg, var(--white), var(--paper));
  }
  .name-band {
    position: absolute; left: 0; top: 119px; width: 325px; height: 38px;
    background: var(--green);
  }
  .person-name {
    position: absolute; left: 34px; top: 124px;
    font-family: "Montserrat", sans-serif; font-weight: 700;
    font-size: 24px; letter-spacing: 1.5px; color: var(--white);
    text-transform: uppercase; line-height: 28px;
  }
  .person-role {
    position: absolute; left: 34px; top: 162px;
    font-family: "Questrial", sans-serif; font-size: 15px; color: var(--text-grey);
  }
  .back-brand {
    position: absolute; left: 335px; top: 116px; width: 222px;
    display: flex; align-items: center; gap: 9px;
  }
  .back-brand .brand-square { width: 30px; height: 30px; background: var(--green); }
  .back-brand .brand-name { font-size: 12.5px; line-height: 1.2; }
  .edge-band {
    position: absolute; right: 0; top: 119px; width: 27px; height: 38px;
    background: var(--green);
  }
  .contact-list {
    position: absolute; left: 34px; top: 242px; list-style: none;
    font-family: "Questrial", sans-serif; font-size: 15.5px; color: var(--text-grey);
  }
  .contact-list li { display: flex; align-items: center; gap: 8px; height: 19px; }
  .contact-list svg { width: 12px; height: 12px; flex: none; }
  .address {
    position: absolute; right: 33px; top: 261px; text-align: right;
    font-family: "Questrial", sans-serif; font-style: normal;
    font-size: 15.5px; line-height: 19px; color: var(--text-grey);
  }
</style>
</head>
<body>
<main class="stage">
  <section class="card card-front" aria-label="Business card side one">
    <div class="front-brand">
      <span class="brand-square" aria-hidden="true"></span>
      <div class="brand-name">Orlend Structural<br>Approval Standards<br>Private Assessors</div>
    </div>
    <div class="front-social">
      <span class="social-square" aria-hidden="true"></span>
      <span>Orlend Structural Approval Standards</span>
    </div>
  </section>

  <section class="card card-back" aria-label="Business card side two">
    <div class="name-band"></div>
    <h1 class="person-name">Daniel Moravi</h1>
    <p class="person-role">Director</p>
    <div class="back-brand">
      <span class="brand-square" aria-hidden="true"></span>
      <div class="brand-name">Orlend Structural<br>Approval Standards<br>Private Assessors</div>
    </div>
    <div class="edge-band"></div>

    <ul class="contact-list">
      <li>
        <svg viewBox="0 0 12 12" aria-hidden="true"><path d="M2.5 1 L4.5 1 L5.2 3.4 L4 4.4 Q5 6.8 7.6 8 L8.6 6.8 L11 7.5 L11 9.5 Q10.5 11 9 11 Q1 10 1 2.8 Q1 1.2 2.5 1 Z" fill="var(--green)"/></svg>
        0431 587 219
      </li>
      <li>
        <svg viewBox="0 0 12 12" aria-hidden="true"><path d="M1 5 L6 1.5 L11 5 L11 11 L1 11 Z" fill="var(--green)"/><path d="M1 5 L6 8.5 L11 5" fill="none" stroke="var(--white)" stroke-width="1"/></svg>
        orlendassessors@mailbox-example.com
      </li>
      <li>
        <svg viewBox="0 0 12 12" aria-hidden="true"><circle cx="6" cy="6" r="5" fill="var(--green)"/><path d="M1 6 H11 M6 1 Q3 6 6 11 Q9 6 6 1" fill="none" stroke="var(--white)" stroke-width="0.8"/></svg>
        www.orlendassessors-example.com.au
      </li>
    </ul>

    <address class="address">7 Tarrunga Rd,<br>Hallworth Vale, SA, 5091</address>
  </section>
</main>
</body>
</html>
```